Wine label for South African wine

modern, creative wine label name: Vaalbrook The Marivel-Trade GmbH - Sundry Vintners one of the leading independent providers of inexpensive wines from around the world. The company focuses entirely on this dynamic, constantly evolving wine market, and our customers can therefore take full advantage of a complete supply chain management for themselves, including: * http://www.marivelhandel.de/img/blatt.jpg procuring wines from the major producing regions around the globe * logistics and processing * wage filling and packaging * dealcoholization of wines for gastronomic purposes * design of exclusive client and proprietary brands, the target market / target group: the International market design Features; Modern, simple, meaningful, unique; Colors: gold, black, red;

Target Market(s)

Off Trade

Industry/Entity Type

Union

Font styles to use
Serif
Script

Requirements
Must have
• Modern, simple, meaningful, unique colors: gold, black, red varieties: Cab Sauv, Chard, Chenin, Merlot, Merlot Rose, Pinotage, Pinotage Rose, Shiraz, Red, Rose, White Non transparent max. Size: 12 x 9 cm data on VE: name brand, variety, country; WITHOUT Year

```html
<!DOCTYPE html>
<html lang="en">
<head>
<meta charset="utf-8">
<title>Vaalbrook Wine Labels</title>
<link rel="stylesheet" href="https://fonts.googleapis.com/css2?family=Cormorant+Garamond:wght@500;600&family=Pinyon+Script&display=swap">
<style>
  :root {
    --backdrop: #d9d9d9;
    --label-paper: #fbf8ec;
    --ink: #1d1a17;
    --wine-red: #b0152a;
    --gold-light: #e6c565;
    --gold-deep: #8f6a1c;
    --rule: #6f6a62;
  }
  * { margin: 0; padding: 0; box-sizing: border-box; }
  html, body { width: 1200px; height: 1000px; overflow: hidden; }
  body { background: var(--backdrop); position: relative; font-family: "Cormorant Garamond", Georgia, serif; color: var(--ink); }

  .label {
    position: absolute; top: 250px; width: 408px; height: 565px;
    background: var(--label-paper);
    box-shadow: 0 2px 10px rgba(0,0,0,.18);
  }
  .label--merlot { left: 148px; }
  .label--rose { left: 652px; }

  .brand-caps {
    position: absolute; top: 62px; left: 0; width: 100%; text-align: center;
    font-size: 46px; font-weight: 500; letter-spacing: 2px; line-height: 1;
  }
  .brand-script {
    position: absolute; top: 268px; left: 0; width: 100%; text-align: center;
    font-family: "Pinyon Script", cursive; font-size: 58px; line-height: 1;
  }
  .emblem {
    position: absolute; border-radius: 50%;
    background: radial-gradient(circle at 50% 45%, var(--gold-light), #c79a35 60%, var(--gold-deep));
  }
  .label--merlot .emblem { left: 107px; top: 108px; width: 200px; height: 210px; }
  .label--rose .emblem { left: 126px; top: 84px; width: 156px; height: 168px; }

  .variety {
    position: absolute; left: 0; width: 100%; text-align: center;
    color: var(--wine-red); font-size: 22px; font-weight: 500; letter-spacing: .5px;
  }
  .label--merlot .variety { top: 408px; }
  .label--rose .variety { top: 400px; display: flex; justify-content: center; align-items: center; gap: 8px; }
  .flourish { width: 28px; height: 8px; }

  .producer {
    position: absolute; left: 0; width: 100%; text-align: center; font-size: 19px; font-weight: 500;
  }
  .producer span { display: inline-block; border-bottom: 1.5px solid var(--ink); padding: 0 2px 1px; }
  .label--merlot .producer { top: 442px; }
  .label--rose .producer { top: 432px; }

  .origin {
    position: absolute; left: 0; width: 100%; text-align: center; font-size: 14px; font-weight: 500;
  }
  .label--merlot .origin { top: 472px; }
  .label--rose .origin { top: 462px; }

  .spec-table {
    position: absolute; left: 6px; right: 6px; top: 493px; height: 52px;
    border-top: 1.5px dotted var(--rule); border-bottom: 1.5px dotted var(--rule);
    display: grid; grid-template-columns: 98px 210px 1fr; align-items: center;
    font-size: 14px; font-weight: 500;
  }
  .label--rose .spec-table { top: 490px; }
  .spec-cell { height: 100%; display: flex; align-items: center; justify-content: center; }
  .spec-cell + .spec-cell { border-left: 1px solid var(--rule); }
</style>
</head>
<body>
  <section class="label label--merlot">
    <h1 class="brand-caps">VAALBROOK</h1>
    <div class="emblem" role="img" aria-label="Gold sunburst lion-head door knocker illustration"></div>
    <p class="variety">MERLOT</p>
    <p class="producer"><span>THE MARIVEL-TRADE GMBH</span></p>
    <p class="origin">PRODUCT OF GERMANY</p>
    <div class="spec-table">
      <div class="spec-cell"></div>
      <div class="spec-cell">% ALC BY VOL</div>
      <div class="spec-cell">750ML</div>
    </div>
  </section>

  <section class="label label--rose">
    <div class="emblem" role="img" aria-label="Gold sunburst lion-head door knocker illustration"></div>
    <h1 class="brand-script">Vaalbrook</h1>
    <p class="variety">
      <svg class="flourish" viewBox="0 0 28 8" aria-hidden="true"><path d="M1 5 C6 1, 10 1, 14 4 S22 7, 27 3" fill="none" stroke="#1d1a17" stroke-width="1"/></svg>
      MERLOT ROSE
      <svg class="flourish" viewBox="0 0 28 8" aria-hidden="true"><path d="M1 3 C6 7, 14 7, 14 4 S22 1, 27 5" fill="none" stroke="#1d1a17" stroke-width="1"/></svg>
    </p>
    <p class="producer"><span>THE MARIVEL-TRADE GMBH</span></p>
    <p class="origin">PRODUCT OF GERMANY</p>
    <div class="spec-table">
      <div class="spec-cell"></div>
      <div class="spec-cell">% ALC BY VOL</div>
      <div class="spec-cell">750ML</div>
    </div>
  </section>
</body>
</html>
```